San Francisco Pet Care Non Profit

Business Card Design for non profit organization.
We are a mobile pet care team who supports and attends to pets whose owners are homeless. Thanks for your help and creativity.

Industry/Entity Type

Non Profit

Contact Information for Business Card

Miriam Loxley
President
2817 Harrow Street, #516
San Francisco, CA 94187
phone: 415-782-3946
fax: 415-718-4053
miriam@warmpawvan.org
website: warmpawvan.org
facebook: facebook.com/WarmPawVan

Font styles to use
Serif
Sans Serif

Colors

Designer to choose colors to be used in the design.

Requirements
Must have
• above details and attached logo

```html
<!DOCTYPE html>
<html lang="en">
<head>
<meta charset="utf-8">
<title>WarmPawVan – Business Card</title>
<link rel="stylesheet" href="https://fonts.googleapis.com/css2?family=Arimo:wght@400;700&display=swap">
<style>
  :root {
    --page-bg: #ecebe8;
    --card-bg: #ffffff;
    --brand-blue: #29a8e0;
    --ink: #1c1c1c;
    --art-blue: #bfe3f5;
    --art-blue-soft: #e3f2fa;
    --art-grey: #efefef;
  }
  * { box-sizing: border-box; margin: 0; padding: 0; }
  html, body {
    width: 900px; height: 1200px; overflow: hidden;
    background: var(--page-bg);
    font-family: "Arimo", Arial, sans-serif;
    color: var(--ink);
  }
  .canvas { position: relative; width: 900px; height: 1200px; }
  .card {
    position: absolute; left: 88px; width: 734px; height: 427px;
    background: var(--card-bg); border-radius: 22px; overflow: hidden;
  }
  .card--front { top: 126px; }
  .card--back { top: 641px; }

  .brand-name {
    position: absolute; font-weight: 700; color: var(--brand-blue);
    letter-spacing: -0.5px; line-height: 1; z-index: 2;
  }
  .tagline { position: absolute; font-weight: 700; color: var(--ink); line-height: 1; z-index: 2; }

  .card--front .brand-name { left: 40px; top: 56px; font-size: 48px; }
  .card--front .tagline { left: 88px; top: 104px; font-size: 20px; }

  .holder-name { position: absolute; left: 42px; top: 158px; font-size: 24px; font-weight: 700; }
  .holder-title { position: absolute; left: 42px; top: 186px; font-size: 17px; font-weight: 700; color: var(--brand-blue); }

  .contact-list { position: absolute; left: 42px; top: 222px; list-style: none; z-index: 2; }
  .contact-item {
    display: flex; align-items: center; height: 29px;
    font-size: 16px; font-weight: 700; white-space: nowrap;
  }
  .contact-icon {
    width: 21px; height: 21px; border-radius: 50%;
    background: var(--brand-blue); margin-right: 12px; flex: none;
    display: flex; align-items: center; justify-content: center;
  }
  .contact-icon svg { width: 13px; height: 13px; fill: #fff; }

  .mascot-art { position: absolute; left: 432px; top: 18px; width: 302px; height: 400px; }
  .mascot-art__head {
    position: absolute; left: 0; top: 0; width: 302px; height: 290px;
    background: linear-gradient(160deg, var(--art-blue), var(--art-blue-soft));
    border-radius: 120px 0 0 60px;
  }
  .mascot-art__body {
    position: absolute; left: 62px; top: 180px; width: 240px; height: 220px;
    background: linear-gradient(180deg, var(--art-blue-soft), var(--art-blue));
    border-radius: 0 0 0 24px;
  }

  .mascot-mini {
    position: absolute; left: 145px; top: 160px; width: 80px; height: 88px;
    background: linear-gradient(160deg, var(--art-blue), var(--art-blue-soft));
    border-radius: 30px 30px 10px 10px;
  }
  .mascot-faint {
    position: absolute; left: 467px; top: 0; width: 267px; height: 427px;
    background: linear-gradient(180deg, var(--art-grey), #f6f6f6);
    border-radius: 110px 0 0 0;
  }
  .card--back .brand-name { left: 245px; top: 182px; font-size: 52px; }
  .card--back .tagline { left: 297px; top: 236px; font-size: 20px; }
  .back-website {
    position: absolute; left: 0; right: 0; top: 366px;
    text-align: center; font-size: 16px; font-weight: 700;
  }
</style>
</head>
<body>
<main class="canvas">

  <section class="card card--front" aria-label="Card front">
    <div class="mascot-art" role="img" aria-label="Mascot illustration: a cat and dog forming a heart atop a small van">
      <div class="mascot-art__head"></div>
      <div class="mascot-art__body"></div>
    </div>

    <div class="brand-name">WarmPawVan</div>
    <div class="tagline">Mobile Pet Care Team</div>

    <div class="holder-name">Miriam Loxley</div>
    <div class="holder-title">President</div>

    <ul class="contact-list">
      <li class="contact-item">
        <span class="contact-icon"><svg viewBox="0 0 24 24"><path d="M6.6 10.8a15 15 0 0 0 6.6 6.6l2.2-2.2a1 1 0 0 1 1-.25 11.4 11.4 0 0 0 3.6.57 1 1 0 0 1 1 1V20a1 1 0 0 1-1 1A17 17 0 0 1 3 4a1 1 0 0 1 1-1h3.5a1 1 0 0 1 1 1c0 1.25.2 2.45.57 3.57a1 1 0 0 1-.25 1z"/></svg></span>
        415-782-3946
      </li>
      <li class="contact-item">
        <span class="contact-icon"><svg viewBox="0 0 24 24"><path d="M6 2h12v5H6zM3 8h18v9h-3v5H6v-5H3zm5 6v6h8v-6z"/></svg></span>
        415-718-4053
      </li>
      <li class="contact-item">
        <span class="contact-icon"><svg viewBox="0 0 24 24"><path d="M2 5h20v14H2zm2 2v.5l8 5 8-5V7l-8 5z"/></svg></span>
        miriam@warmpawvan.org
      </li>
      <li class="contact-item">
        <span class="contact-icon"><svg viewBox="0 0 24 24"><path d="M12 2a10 10 0 1 0 0 20 10 10 0 0 0 0-20zm0 2c1 1.2 1.8 3 2.1 5H9.9C10.2 7 11 5.2 12 4zM4.3 11h3.6c0 .7 0 1.3.1 2H4.3a8 8 0 0 1 0-2zm5.6 0h4.2a17 17 0 0 1 0 2H9.9a17 17 0 0 1 0-2zm6.2 0h3.6a8 8 0 0 1 0 2h-3.6c.1-.7.1-1.3 0-2zM9.9 15h4.2c-.3 2-1.1 3.8-2.1 5-1-1.2-1.8-3-2.1-5z"/></svg></span>
        www.warmpawvan.org
      </li>
      <li class="contact-item">
        <span class="contact-icon"></span>
        WarmPawVan
      </li>
      <li class="contact-item">
        <span class="contact-icon"><svg viewBox="0 0 24 24"><path d="M12 2a7 7 0 0 0-7 7c0 5 7 13 7 13s7-8 7-13a7 7 0 0 0-7-7zm0 9.5A2.5 2.5 0 1 1 12 6.5a2.5 2.5 0 0 1 0 5z"/></svg></span>
        2817 Harrow Street, #516, San Francisco, CA 94187
      </li>
    </ul>
  </section>

  <section class="card card--back" aria-label="Card back">
    <div class="mascot-faint" role="img" aria-label="Faint oversized mascot illustration as background decoration"></div>
    <div class="mascot-mini" role="img" aria-label="Small mascot illustration: cat and dog heart on a van"></div>
    <div class="brand-name">WarmPawVan</div>
    <div class="tagline">Mobile Pet Care Team</div>
    <div class="back-website">www.warmpawvan.org</div>
  </section>

</main>
</body>
</html>
```